Visitenkarten-Design Neutrale Verzollungs Agentur für den Grenzverkehr des Zollwesens
Sehr schnelle Umsetzung nach unserer Vorstellung,und sehr netter und guter Umgang in der Kominikation. tolvix hat unsere erwartung zu 100 % übertroffen.
Zielgruppe
Wir sind eine Neutrale Verzollungs Agentur für den Grenzverkehr des Zollwesens
Bluefield & Meridian Group
Wir führen für Kunden die Zollabwicklungen ab.
Seefracht - Bahnfracht-Luftfracht-LKW Fracht
Cargo - Hersteller Firmen und Endknden International
Aufgabenstellung
Rückseite sollte mitgestaltet werden

```html
<!DOCTYPE html>
<html lang="de">
<head>
<meta charset="utf-8">
<title>Grenzwerk – Visitenkarten</title>
<link href="https://fonts.googleapis.com/css2?family=Source+Sans+3:wght@600;700&display=swap" rel="stylesheet">
<style>
  :root {
    --board: #c6c6c6;
    --paper: #ffffff;
    --navy: #1a365a;
    --ink: #555555;
    --wordmark: #4e4e4e;
    --wordmark-dark: #5a5a5a;
    --blue: #3a8ad6;
    --blue-light: #a9ccef;
    --photo-sky: #c9cdd2;
    --photo-ground: #8a9096;
  }
  * { box-sizing: border-box; margin: 0; padding: 0; }
  html, body { width: 1200px; height: 1200px; overflow: hidden; }
  body {
    background: var(--board);
    font-family: "Source Sans 3", "Segoe UI", sans-serif;
    position: relative;
  }
  .card {
    position: absolute;
    width: 419px;
    height: 272px;
    overflow: hidden;
    box-shadow: 3px 4px 6px rgba(0,0,0,0.35);
  }
  .card--front { left: 390px; top: 205px; background: var(--paper); }
  .card--back  { left: 151px; top: 599px; background: var(--navy); }
  .card--photo { left: 627px; top: 594px; background: var(--navy); }

  .wordmark {
    position: absolute;
    left: 0; right: 0;
    display: flex;
    align-items: center;
    justify-content: center;
    gap: 10px;
    font-weight: 600;
    color: var(--wordmark);
    letter-spacing: 0.5px;
  }
  .wordmark__dot {
    width: 0.55em; height: 0.55em;
    border-radius: 50%;
    background: var(--blue);
  }
  .card--front .wordmark { top: 55px; font-size: 38px; }
  .card--back .wordmark { top: 108px; font-size: 46px; color: var(--wordmark-dark); }
  .card--photo .wordmark { top: 38px; left: 90px; right: 0; font-size: 32px; }

  .details {
    position: absolute;
    left: 0; right: 0; top: 172px;
    text-align: center;
    color: var(--ink);
  }
  .details__company { font-size: 17px; font-weight: 700; line-height: 22px; }
  .details__regions { font-size: 13.5px; font-weight: 700; line-height: 22px; }
  .details__regions .sep { color: var(--blue); font-weight: 600; }
  .details__contact {
    font-size: 12.5px; font-weight: 700; line-height: 22px;
    display: flex; justify-content: center; gap: 10px;
  }
  .details__contact span { display: inline-flex; align-items: center; gap: 3px; }
  .details__contact svg { width: 9px; height: 9px; }

  .band {
    position: absolute;
    left: 0; bottom: 0;
    width: 100%; height: 17px;
    background: linear-gradient(90deg, var(--blue-light) 0%, var(--blue) 45%, var(--blue) 100%);
  }
  .band svg { position: absolute; left: 14px; top: 0; }

  .card--photo svg.photo-layout { position: absolute; inset: 0; }
</style>
</head>
<body>

  <section class="card card--front" aria-label="Visitenkarte Vorderseite">
    <div class="wordmark"><span class="wordmark__dot"></span>Grenzwerk</div>
    <div class="details">
      <p class="details__company">Bluefield &amp; Meridian Group</p>
      <p class="details__regions">Switzerland <span class="sep">|</span> Germany <span class="sep">|</span> Denmark <span class="sep">|</span> France</p>
      <p class="details__contact">
        <span>
          <svg viewBox="0 0 10 10"><rect x="0.5" y="2" width="9" height="6.5" rx="1" fill="#3a8ad6"/><path d="M0.8 2.4 L5 5.6 L9.2 2.4" stroke="#fff" stroke-width="1" fill="none"/></svg>
          service@grenzwerk-beispiel.de
        </span>
        <span>
          <svg viewBox="0 0 10 10"><circle cx="5" cy="5" r="4.5" fill="#3a8ad6"/><path d="M0.5 5 H9.5 M5 0.5 V9.5" stroke="#fff" stroke-width="0.8"/><ellipse cx="5" cy="5" rx="2" ry="4.5" stroke="#fff" stroke-width="0.8" fill="none"/></svg>
          www.grenzwerk-beispiel.de
        </span>
      </p>
    </div>
    <div class="band">
      <svg width="50" height="17" viewBox="0 0 50 17">
        <g fill="#ffffff">
          <polygon points="8,0 12,0 4,17 0,17"/>
          <polygon points="18,0 22,0 14,17 10,17"/>
          <polygon points="28,0 32,0 24,17 20,17"/>
          <polygon points="38,0 42,0 34,17 30,17"/>
        </g>
      </svg>
    </div>
  </section>

  <section class="card card--back" aria-label="Visitenkarte Rückseite">
    <div class="wordmark"><span class="wordmark__dot"></span>Grenzwerk</div>
  </section>

  <section class="card card--photo" aria-label="Visitenkarte Rückseite mit Bild">
    <svg class="photo-layout" width="420" height="273" viewBox="0 0 420 273">
      <defs>
        <linearGradient id="photoTone" x1="0" y1="0" x2="0" y2="1">
          <stop offset="0" stop-color="#cdd1d6"/>
          <stop offset="0.7" stop-color="#bcc1c7"/>
          <stop offset="1" stop-color="#8a9096"/>
        </linearGradient>
      </defs>
      <polygon points="128,0 420,0 287,273 0,273" fill="url(#photoTone)" role="img" aria-label="Foto: Passagierflugzeug beim Start über einem Flughafen"/>
    </svg>
    <div class="wordmark"><span class="wordmark__dot"></span>Grenzwerk</div>
  </section>

</body>
</html>
```